Print on top the name of the company: (Or Similar)
Larkmoor Cleaning & Disinfecting
Because your standards aren't standard.

We adhere to ALL NVB guidelines for both residential and commercial cleaning.

Infection Control is our ultimate goal.

Instructions:
Opening a residential and commercial cleaning and disinfecting company in south Florida.

Targeting high-end residential clients, commercial and healthcare facilities, specializing in Ambulatory Care Guidelines. With a concentration and expertise in targeting Covid 19 and other transmissible pathogens.

UMRE trained.
Owned and operated by a licensed BSN Registered Nurse specially ​trained in Infection Control Prevention with over 25 years experience. Over two decades in Ambulatory Surgery Center Administration, Director of Nursing and Infection Control Prevention ad Consulting.

Looking to create a business flier that emphasizes Cleaning & Disinfection
along with the standard expectation for residential and Commercial cleaning services
Updates

Need extra days to review

Target Market(s)

Residential & Commercial

Font styles to use
Decorative

Requirements
Must have
• A checklist for cleaning services

```html
<!DOCTYPE html>
<html lang="en">
<head>
<meta charset="utf-8">
<title>Larkmoor Cleaning &amp; Disinfecting</title>
<link rel="stylesheet" href="https://fonts.googleapis.com/css2?family=Almendra:ital,wght@0,400;0,700;1,400;1,700&display=swap">
<style>
  :root {
    --yellow: #fff200;
    --red: #ed1c24;
    --blue: #1eaeea;
    --ink: #1a1a1a;
    --white: #ffffff;
    --room-light: #eef0f1;
    --room-mid: #c9cdd0;
    --room-grey: #a9aeb2;
  }
  html, body { margin: 0; padding: 0; overflow: hidden; }
  body { width: 1200px; height: 802px; background: var(--white); }
  .flyer {
    position: relative;
    width: 1200px;
    height: 802px;
    overflow: hidden;
    font-family: "Almendra", serif;
  }
  .scene-photo {
    position: absolute; inset: 0;
    background:
      radial-gradient(ellipse at 85% 60%, rgba(40,110,70,0.35), transparent 35%),
      radial-gradient(ellipse at 20% 30%, #ffffff, transparent 45%),
      linear-gradient(180deg, var(--room-mid) 0%, var(--room-grey) 45%, var(--room-light) 75%, #f4f4f4 100%);
  }
  .shapes { position: absolute; inset: 0; }
  .brand-title {
    position: absolute; left: 0; right: 0; top: 10px;
    margin: 0; text-align: center;
    font-weight: 700; font-style: italic;
    font-size: 62px; line-height: 1;
    color: var(--white);
    text-shadow: 2px 3px 3px rgba(0,0,0,0.45);
    letter-spacing: 1px;
  }
  .tagline {
    position: absolute; left: 138px; top: 134px;
    margin: 0;
    font-style: italic; font-weight: 700;
    font-size: 24px; line-height: 1;
    white-space: nowrap;
    color: var(--blue);
    transform: rotate(-2.3deg);
    transform-origin: left center;
  }
  .instructions {
    position: absolute; left: 34px; top: 346px; width: 360px;
    color: var(--ink); font-style: italic;
    font-size: 17px; line-height: 24px;
  }
  .instructions h2 {
    margin: 0 0 8px; font-size: 27px; line-height: 30px; font-weight: 700; font-style: italic;
  }
  .instructions p { margin: 0 0 24px; position: relative; }
  .instructions .bullet {
    position: absolute; left: -22px; top: 5px; width: 18px; height: 14px;
  }
  .promise {
    position: absolute; left: 553px; top: 364px; width: 186px;
    text-align: center; color: var(--blue);
    font-style: italic; font-weight: 700;
    font-size: 20px; line-height: 27px;
  }
  .promise p { margin: 0 0 18px; }
  .checklist {
    position: absolute; left: 880px; top: 158px; width: 300px;
    color: var(--ink); font-style: italic;
  }
  .checklist h2 {
    margin: 0 0 6px; font-size: 24px; line-height: 28px; font-weight: 700;
  }
  .checklist ul { list-style: none; margin: 0; padding: 0; }
  .checklist li {
    position: relative; padding-left: 26px;
    font-size: 17px; line-height: 26px; font-weight: 700;
  }
  .checklist .tick {
    position: absolute; left: 0; top: 6px; width: 18px; height: 15px;
  }
  .phone {
    position: absolute; left: 522px; top: 742px; width: 380px;
    text-align: center; margin: 0;
    font-style: italic; font-weight: 700;
    font-size: 50px; line-height: 1;
    color: var(--white);
    text-shadow: 2px 3px 3px rgba(0,0,0,0.4);
  }
</style>
</head>
<body>
<main class="flyer">
  <div class="scene-photo" role="img" aria-label="Photo of a cleaning team in uniforms tidying a bright living room, one worker vacuuming the carpet"></div>

  <svg class="shapes" width="1200" height="802" viewBox="0 0 1200 802" aria-hidden="true">
    <path d="M0,66 Q600,140 1200,60 L1200,0 L0,0 Z" fill="var(--red)"/>
    <path d="M0,92 Q620,118 1200,82 L1200,112 Q620,132 0,116 Z" fill="var(--blue)"/>
    <path d="M0,70 Q600,112 1200,64 L1200,86 Q620,124 0,96 Z" fill="var(--red)"/>
    <path d="M0,0 L1200,0 L1200,62 Q620,110 0,66 Z" fill="var(--yellow)"/>

    <path d="M40,108 L150,120 L140,174 L58,154 L80,132 Z" fill="var(--red)"/>
    <path d="M560,112 L680,120 L660,152 L680,170 L560,162 Z" fill="var(--red)"/>
    <path d="M108,128 L606,108 L612,146 L114,166 Z" fill="var(--white)" stroke="var(--blue)" stroke-width="4"/>

    <path d="M0,338 Q150,270 300,300 Q470,350 490,600 Q495,720 420,802 L0,802 Z" fill="var(--red)"/>
    <path d="M0,352 Q150,288 296,316 Q456,362 474,600 Q478,718 404,802 L0,802 Z" fill="var(--blue)"/>
    <path d="M0,366 Q150,304 292,330 Q442,374 460,600 Q464,716 390,802 L0,802 Z" fill="rgba(255,255,255,0.88)"/>

    <circle cx="654" cy="458" r="136" fill="var(--red)"/>
    <circle cx="646" cy="456" r="132" fill="var(--yellow)"/>

    <path d="M410,802 Q500,700 760,690 Q1000,694 1090,802 Z" fill="var(--red)"/>
    <path d="M424,802 Q510,712 760,702 Q990,706 1076,802 Z" fill="var(--blue)"/>
    <path d="M442,802 Q520,724 760,716 Q980,720 1058,802 Z" fill="var(--yellow)"/>
  </svg>

  <h1 class="brand-title">Larkmoor Cleaning &amp; Disinfecting</h1>
  <p class="tagline">Because your standards aren't standard.</p>

  <section class="instructions">
    <h2>Instructions:</h2>
    <p><svg class="bullet" viewBox="0 0 18 14"><path d="M0,0 L18,7 L0,14 L5,7 Z" fill="var(--red)"/></svg>Opening a residential and commercial cleaning and disinfecting company in south Florida.</p>
    <p><svg class="bullet" viewBox="0 0 18 14"><path d="M0,0 L18,7 L0,14 L5,7 Z" fill="var(--red)"/></svg>Targeting high-end residential clients, commercial and healthcare facilities, specializing in Ambulatory Care Guidelines. With a concentration and expertise in targeting Covid 19 and other transmissible pathogens.</p>
    <p><svg class="bullet" viewBox="0 0 18 14"><path d="M0,0 L18,7 L0,14 L5,7 Z" fill="var(--red)"/></svg>UMRE trained.<br>Owned and operated by a licensed BSN Registered Nurse specially trained in Infection Control Prevention with over 25 years experience. Over two decades in Ambulatory Surgery Center Administration, Director of Nursing and Infection Control Prevention ad Consulting.</p>
  </section>

  <section class="promise">
    <p>We adhere to ALL NVB guidelines for both residential and commercial cleaning.</p>
    <p>Infection Control is our ultimate goal.</p>
  </section>

  <section class="checklist">
    <h2>Our Cleaning Checklist</h2>
    <ul>
      <li><svg class="tick" viewBox="0 0 18 15"><path d="M1,8 L7,13 L17,2" fill="none" stroke="var(--red)" stroke-width="3"/></svg>Dusting &amp; wiping all surfaces</li>
      <li><svg class="tick" viewBox="0 0 18 15"><path d="M1,8 L7,13 L17,2" fill="none" stroke="var(--red)" stroke-width="3"/></svg>Vacuuming &amp; mopping floors</li>
      <li><svg class="tick" viewBox="0 0 18 15"><path d="M1,8 L7,13 L17,2" fill="none" stroke="var(--red)" stroke-width="3"/></svg>Kitchen &amp; bathroom sanitizing</li>
      <li><svg class="tick" viewBox="0 0 18 15"><path d="M1,8 L7,13 L17,2" fill="none" stroke="var(--red)" stroke-width="3"/></svg>High-touch point disinfection</li>
      <li><svg class="tick" viewBox="0 0 18 15"><path d="M1,8 L7,13 L17,2" fill="none" stroke="var(--red)" stroke-width="3"/></svg>Trash removal &amp; restocking</li>
    </ul>
  </section>

  <p class="phone">(555) 304-18-92</p>
</main>
</body>
</html>
```